Etiketten-Design für Tee-Standbeutel
Zielgruppe
Wir sind ein kleines Café in dem unsere Gäste nicht nur den Kaffee sondern auch unsere natürlichen Tees lieben. Da immer wieder die Nachfrage nach den Tees bestand, möchten wir jetzt den Tee in Standbodenbeutel anbieten.
Kundschaft: Ab 25 Jahre, überwiegend weiblich, Affinität zu Yoga, Wellness, Körperbewusstsein, Gesundheitsbewusst, Premium Tee´s, Entspannung, Meditation, gesunde Ernährung.
Aufgabenstellung
Vorab:
Uns ist wichtig, das auch nach dem Entwurf mit dem Designer zusammen gearbeitet wird. Wenn neue Verpackungen hinzukommen und die Etiketten für die Rückseite gestaltet werden, dann soll dies aus einer Hand kommen.
LogoName:
Kelbinger – Blatt & Sud – Logo von Kelbinger existiert bereits, Blatt & Sud müsste angepasst werden.
Die Idee kam daher, das ich ein Cafe betreibe und die Gäste den Tee gerne auch für zuhause kaufen würden.
Kundschaft:
Ab 25 Jahre, überwiegend weiblich, Affinität zu Yoga, Wellness, Körperbewusstsein, Gesundheitsbewusst, Premium Tee´s, Entspannung, Meditation, gesunde Ernährung
Verpackungsgröße:
kleine Verpackung: 110x185+70mm 250ml/125g
große Verpackung: 130x225+80mm 500ml/ 250g
Das Etikett soll sowohl bei der kleinen als auch bei der großen Packung verwendet werden.
Verpackung:
ist schwarz – Doy Verpackung;
evtl. später Dosen in schwarz
Idee:
Es sind anfänglich ca. 6 verschiedene Teesorten geplant. Etikett soll durch verschiedene Farben den Inhalt des Tees oder Gewürz widerspiegeln
z.B. schwarzer Tee – grau, Kräutertees – grün, Früchtetee – rot, …
Tees:
Verschiedene Kräutertees und Gewürze
Stil:
unkonventionell, individuell, authentisch und alles – außer gewöhnlich
Stil des Sozialrealismus z.B. Jalmar - Limonade
kultiges Underground Image
extravagant und anders, hervorhebend
urban style
oder aber:
filigran, schwedischer Stil, helle Farben, dezent und trotzdem ausdrucksstark, einladend

```html
<!DOCTYPE html>
<html lang="de">
<head>
<meta charset="utf-8">
<title>Kelbinger – Tee-Etiketten</title>
<link rel="stylesheet" href="https://fonts.googleapis.com/css2?family=Montserrat:wght@700&family=Josefin+Sans:wght@400;600&family=Great+Vibes&display=swap">
<style>
  :root {
    --paper: #ffffff;
    --label-grey: #d7d7d7;
    --skin: #b07a52;
    --shadow-purple: #3a2440;
    --black-panel: #262626;
    --black-word: #4b4b4b;
    --black-shirt: #5e5e5e;
    --fruit-panel: #44151f;
    --fruit-word: #6d1020;
    --fruit-shirt: #7a1526;
    --herb-panel: #313a24;
    --herb-word: #435128;
    --herb-shirt: #4f6430;
    --ink: #333333;
  }
  * { box-sizing: border-box; margin: 0; padding: 0; }
  html, body {
    width: 1200px; height: 597px; overflow: hidden;
    background: var(--paper);
  }
  .sheet { position: relative; width: 1200px; height: 597px; }
  .label {
    position: absolute; top: 0; width: 390px; height: 597px;
  }
  .label--black { left: 5px; --panel: var(--black-panel); --word: var(--black-word); --shirt: var(--black-shirt); }
  .label--fruit { left: 407px; --panel: var(--fruit-panel); --word: var(--fruit-word); --shirt: var(--fruit-shirt); }
  .label--herb  { left: 808px; --panel: var(--herb-panel); --word: var(--herb-word); --shirt: var(--herb-shirt); }

  .label__side {
    position: absolute; left: 0; top: 0; width: 166px; height: 597px;
    background: var(--label-grey); overflow: hidden;
  }
  .label__figure {
    position: absolute; left: 0; top: 172px; width: 158px; height: 425px;
    border-radius: 60px 40px 0 0;
    background: linear-gradient(180deg, #3b2a20 0%, var(--skin) 18%, var(--shirt) 40%, var(--skin) 62%, var(--shadow-purple) 85%, #1e1626 100%);
    opacity: .92;
  }
  .label__word { position: absolute; left: 0; top: 0; }
  .label__word text {
    font-family: "Montserrat", sans-serif; font-weight: 700;
    fill: var(--word);
  }

  .label__panel {
    position: absolute; left: 166px; top: 0; width: 224px; height: 597px;
    background: var(--panel); color: var(--paper);
  }
  .label__frame {
    position: absolute; inset: 9px 9px 9px 9px;
    border: 2px solid var(--paper);
  }
  .brand {
    position: absolute; left: 22px; top: 214px; width: 181px; height: 68px;
    background: var(--paper);
    display: flex; align-items: center; justify-content: center;
    font-family: "Josefin Sans", sans-serif; font-weight: 400;
    font-size: 31px; letter-spacing: 1px; color: var(--ink);
    text-transform: uppercase;
  }
  .tea-name {
    position: absolute; left: 0; top: 336px; width: 224px; text-align: center;
    font-family: "Great Vibes", cursive; font-size: 28px; line-height: 1;
  }
  .tea-text {
    position: absolute; left: 20px; top: 378px; width: 184px; text-align: center;
    font-family: "Josefin Sans", sans-serif; font-size: 13.5px; line-height: 15.5px;
  }
  .tea-volume {
    position: absolute; left: 0; top: 565px; width: 224px; text-align: center;
    font-family: "Josefin Sans", sans-serif; font-size: 11.5px;
  }
</style>
</head>
<body>
<main class="sheet">

  <section class="label label--black">
    <div class="label__side">
      <div class="label__figure" role="img" aria-label="Illustration einer meditierenden Frau im Schneidersitz, graues Shirt"></div>
      <svg class="label__word" width="166" height="597" viewBox="0 0 166 597" aria-hidden="true">
        <text transform="translate(163 540) rotate(-90)" font-size="108" textLength="540" lengthAdjust="spacingAndGlyphs">SCHWARZ</text>
      </svg>
    </div>
    <div class="label__panel">
      <div class="label__frame"></div>
      <div class="brand">Kelbinger</div>
      <h2 class="tea-name">Feiner Schwarztee</h2>
      <p class="tea-text">Dieser Schwarztee überzeugt durch seine besondere Würze aus handverlesenen Teeblättern.</p>
      <p class="tea-volume">Inhalt: 250 ml / 125 g</p>
    </div>
  </section>

  <section class="label label--fruit">
    <div class="label__side">
      <div class="label__figure" role="img" aria-label="Illustration einer meditierenden Frau im Schneidersitz, rotes Shirt"></div>
      <svg class="label__word" width="166" height="597" viewBox="0 0 166 597" aria-hidden="true">
        <text transform="translate(163 540) rotate(-90)" font-size="108" textLength="540" lengthAdjust="spacingAndGlyphs">FRÜCHTE</text>
      </svg>
    </div>
    <div class="label__panel">
      <div class="label__frame"></div>
      <div class="brand">Kelbinger</div>
      <h2 class="tea-name">Feiner Früchtetee</h2>
      <p class="tea-text">Dieser Früchtetee überzeugt durch seine besonderes Aroma aus handverlesenen Früchten.</p>
      <p class="tea-volume">Inhalt: 250 ml / 125 g</p>
    </div>
  </section>

  <section class="label label--herb">
    <div class="label__side">
      <div class="label__figure" role="img" aria-label="Illustration einer meditierenden Frau im Schneidersitz, grünes Shirt"></div>
      <svg class="label__word" width="166" height="597" viewBox="0 0 166 597" aria-hidden="true">
        <text transform="translate(163 540) rotate(-90)" font-size="108" textLength="540" lengthAdjust="spacingAndGlyphs">KRÄUTER</text>
      </svg>
    </div>
    <div class="label__panel">
      <div class="label__frame"></div>
      <div class="brand">Kelbinger</div>
      <h2 class="tea-name">Feiner Kräutertee</h2>
      <p class="tea-text">Dieser Kräutertee überzeugt durch seine besonderes Aroma aus handverlesenen Kräutern.</p>
      <p class="tea-volume">Inhalt: 250 ml / 125 g</p>
    </div>
  </section>

</main>
</body>
</html>
```